CD-/Plattencover für Tonträgerfirma
Zielgruppe
Wir sind eine Tonträgerfirma und bewegen uns im Low-Budget-Segment.
Aufgabenstellung
Für eine KLassik Serie benötigen wir 7 Cover, welche aber im Grundlayout immer gleich seinen sollten. Es soll eine erkenntliche Serie entstehen.
Das Thema lautet: Velvet Hour
Die Unterthemen lauten:
1. The Amber Lantern Gathering
2. The Velvet Hour Riverside Suites
3. The Velvet Hour Meadow Steps
4. The Velvet Hour Moonlit Whispers
5. The Copper Table Evenings
6. The Silver Curtain Soirée
7. The Northwind Orchestral Treasures
Wir benötigen nicht das komplette Artwork, sondern ein Frontcover
(12 x 12 cm + 2 cm Beschnitt wg. etwaiger Verschiebung der Positionierung
Fertigstellung (Aufziehen des Inlays und Labels) erfolgt später bei uns im Hause
Wir benötigen später offene psd-Dateien mit allen Ebenen
Wichtig: Schriften nicht gerastert ggfs. Schrift mitliefern

```html
<!DOCTYPE html>
<html lang="en">
<head>
<meta charset="utf-8">
<title>Velvet Hour – Cover Series</title>
<link rel="stylesheet" href="https://fonts.googleapis.com/css2?family=Roboto+Slab:wght@200;900&display=swap">
<style>
  :root {
    --sheet: #ffffff;
    --cover-pink: #f4a9b4;
    --lime: #8fe01a;
    --lavender: #c9b0f2;
    --indigo: #5a5cc8;
    --yellow: #f2f20a;
    --orchid: #f5a6ee;
    --rose: #f25a8c;
    --cover-size: 371px;
  }
  * { box-sizing: border-box; margin: 0; padding: 0; }
  html, body {
    width: 808px; height: 1200px; overflow: hidden;
    background: var(--sheet);
  }
  .series {
    position: relative; width: 808px; height: 1200px;
  }
  .cover {
    position: absolute; width: var(--cover-size); height: var(--cover-size);
    background: var(--cover-pink); overflow: hidden;
    font-family: "Roboto Slab", serif;
  }
  .cover--amber    { left: 22px;  top: 22px; }
  .cover--riverside{ left: 413px; top: 22px; }
  .cover--moonlit  { left: 22px;  top: 414px; }
  .cover--copper   { left: 413px; top: 414px; }
  .cover--silver   { left: 22px;  top: 804px; }
  .cover--meadow   { left: 413px; top: 804px; }

  .portrait-art {
    position: absolute; left: 0; top: 10px; width: 330px; height: 361px;
    border-radius: 0 150px 0 0;
  }
  .cover--amber .portrait-art {
    background: radial-gradient(ellipse 38% 42% at 52% 45%, #ffffff 60%, rgba(255,255,255,0) 100%),
                linear-gradient(135deg, #d8141c 0%, #2f9d3a 30%, #e8701a 60%, #c81430 100%);
  }
  .cover--riverside .portrait-art {
    background: radial-gradient(ellipse 38% 42% at 52% 45%, #ffffff 60%, rgba(255,255,255,0) 100%),
                linear-gradient(135deg, #6a1aa8 0%, #22b07a 35%, #1e9be8 65%, #5b1e9e 100%);
  }
  .cover--moonlit .portrait-art {
    background: radial-gradient(ellipse 38% 42% at 52% 45%, #ffffff 60%, rgba(255,255,255,0) 100%),
                linear-gradient(135deg, #c08a1c 0%, #e1d98a 35%, #9ee07a 60%, #b8841a 100%);
  }
  .cover--copper .portrait-art {
    background: radial-gradient(ellipse 38% 42% at 52% 45%, #ffffff 60%, rgba(255,255,255,0) 100%),
                linear-gradient(135deg, #a818b8 0%, #20a860 35%, #20c0e8 65%, #a01ab0 100%);
  }
  .cover--silver .portrait-art {
    background: radial-gradient(ellipse 38% 42% at 52% 45%, #ffffff 60%, rgba(255,255,255,0) 100%),
                linear-gradient(135deg, #d8141c 0%, #30d060 35%, #28b048 60%, #c01428 100%);
  }
  .cover--meadow .portrait-art {
    background: radial-gradient(ellipse 38% 42% at 52% 45%, #ffffff 60%, rgba(255,255,255,0) 100%),
                linear-gradient(135deg, #7a2ac0 0%, #f06a9a 35%, #c070e0 65%, #6a22b0 100%);
  }

  .cover-title {
    position: absolute; text-transform: uppercase; line-height: 0.92;
    color: var(--title-colour);
  }
  .cover-title span { display: block; white-space: nowrap; }
  .cover-title .light { font-weight: 200; }
  .cover-title .bold { font-weight: 900; }

  .cover-title--vertical {
    writing-mode: vertical-rl; transform: rotate(180deg);
    left: 8px; bottom: 12px; font-size: 31px;
  }
  .cover-title--horizontal {
    left: 8px; font-size: 31px;
  }

  .cover--amber .cover-title    { --title-colour: var(--lime); }
  .cover--riverside .cover-title{ --title-colour: var(--lavender); top: 172px; }
  .cover--moonlit .cover-title  { --title-colour: var(--indigo); top: 266px; }
  .cover--copper .cover-title   { --title-colour: var(--yellow); }
  .cover--silver .cover-title   { --title-colour: var(--orchid); }
  .cover--meadow .cover-title   { --title-colour: var(--rose); top: 266px; }
</style>
</head>
<body>
  <main class="series">
    <section class="cover cover--amber">
      <div class="portrait-art" role="img" aria-label="Pop-art portrait of a composer in red, green and orange with halftone dots and small birds"></div>
      <h2 class="cover-title cover-title--vertical">
        <span class="light">The Amber</span>
        <span class="bold">Lantern</span>
        <span class="light">Gathering</span>
      </h2>
    </section>

    <section class="cover cover--riverside">
      <div class="portrait-art" role="img" aria-label="Pop-art portrait of a composer in purple, green and blue with halftone dots and small birds"></div>
      <h2 class="cover-title cover-title--horizontal">
        <span class="light">The Velvet Hour</span>
        <span class="bold">Riverside</span>
        <span class="light">Suites</span>
      </h2>
    </section>

    <section class="cover cover--moonlit">
      <div class="portrait-art" role="img" aria-label="Pop-art portrait of a composer in ochre, pale yellow and light green with halftone dots and small birds"></div>
      <h2 class="cover-title cover-title--horizontal">
        <span class="light">The Velvet Hour</span>
        <span class="bold">Moonlit</span>
        <span class="light">Whispers</span>
      </h2>
    </section>

    <section class="cover cover--copper">
      <div class="portrait-art" role="img" aria-label="Pop-art portrait of a composer in magenta, green and cyan with halftone dots and small birds"></div>
      <h2 class="cover-title cover-title--vertical">
        <span class="light">The Copper</span>
        <span class="bold">Table</span>
        <span class="light">Evenings</span>
      </h2>
    </section>

    <section class="cover cover--silver">
      <div class="portrait-art" role="img" aria-label="Pop-art portrait of a composer in red and bright green with halftone dots and small birds"></div>
      <h2 class="cover-title cover-title--vertical">
        <span class="light">The Silver</span>
        <span class="bold">Curtain</span>
        <span class="light">Soirée</span>
      </h2>
    </section>

    <section class="cover cover--meadow">
      <div class="portrait-art" role="img" aria-label="Pop-art portrait of a composer in violet, pink and lilac with halftone dots and small birds"></div>
      <h2 class="cover-title cover-title--horizontal">
        <span class="light">The Velvet Hour</span>
        <span class="bold">Meadow</span>
        <span class="light">Steps</span>
      </h2>
    </section>
  </main>
</body>
</html>
```